Business Card Design Project

"Pine Ledger Systems" is database management company working in the direct marketing & digital printing industries. Currently going through a name & rebranding process we require a new company business card.

Industry/Entity Type

Marketing

```html
<!DOCTYPE html>
<html lang="en">
<head>
<meta charset="utf-8">
<title>Pine Ledger Systems – Business Card</title>
<link rel="stylesheet" href="https://fonts.googleapis.com/css2?family=Arimo:wght@400;700&display=swap">
<style>
  :root {
    --backdrop: #e6e2dc;
    --card: #ffffff;
    --ink: #4d5057;
    --ink-soft: #5b5e65;
    --blue: #1ba3e3;
    --blue-deep: #1681cf;
    --slate: #5a5f6a;
  }
  * { margin: 0; padding: 0; box-sizing: border-box; }
  html, body { width: 1155px; height: 1200px; overflow: hidden; }
  body {
    background: var(--backdrop);
    font-family: "Arimo", Arial, sans-serif;
    color: var(--ink);
    position: relative;
  }
  .card {
    position: absolute;
    left: 168px;
    width: 820px;
    height: 466px;
    background: var(--card);
    border-radius: 16px;
    overflow: hidden;
    box-shadow: 0 4px 14px rgba(0,0,0,0.18);
  }
  .card--front { top: 88px; }
  .card--back { top: 590px; }

  /* front: plain vertical edge bars */
  .edge-bar {
    position: absolute;
    top: 0;
    bottom: 0;
    right: 0;
    width: 34px;
    background: linear-gradient(180deg, var(--blue), var(--blue-deep));
  }
  .edge-rule {
    position: absolute;
    top: 0;
    bottom: 0;
    right: 44px;
    width: 6px;
    background: var(--slate);
  }

  /* back: plain footer band */
  .footer-band {
    position: absolute;
    left: 0;
    right: 0;
    bottom: 0;
    height: 62px;
    background: linear-gradient(90deg, var(--blue-deep), var(--blue));
  }
  .footer-rule {
    position: absolute;
    left: 0;
    right: 0;
    bottom: 72px;
    height: 6px;
    background: var(--slate);
  }

  .brand {
    position: absolute;
    display: flex;
    align-items: center;
    gap: 12px;
    font-weight: 700;
    color: var(--ink-soft);
    white-space: nowrap;
  }
  .brand__mark { background: var(--blue); flex: none; }
  .card--front .brand { left: 372px; top: 68px; font-size: 30px; }
  .card--front .brand__mark { width: 22px; height: 22px; }
  .card--back .brand { left: 86px; top: 134px; font-size: 52px; gap: 18px; }
  .card--back .brand__mark { width: 36px; height: 36px; }

  .contact {
    position: absolute;
    left: 54px;
    top: 158px;
    font-size: 17px;
    line-height: 26px;
    font-style: normal;
    color: var(--ink);
  }
  .contact__address { font-weight: 700; }
  .contact__list { list-style: none; }
  .contact__item { display: flex; align-items: center; gap: 10px; }
  .contact__icon { width: 16px; height: 16px; flex: none; fill: var(--blue); }

  .person { position: absolute; left: 438px; top: 208px; }
  .person__name { font-size: 40px; font-weight: 700; color: var(--ink-soft); line-height: 1.1; }
  .person__role { font-size: 26px; color: var(--ink-soft); margin-top: 4px; }

  .website {
    position: absolute;
    left: 210px;
    top: 292px;
    font-size: 18px;
    color: var(--ink);
  }
</style>
</head>
<body>

<section class="card card--front">
  <div class="edge-rule" aria-hidden="true"></div>
  <div class="edge-bar" aria-hidden="true"></div>

  <div class="brand"><span class="brand__mark"></span>Pine Ledger Systems</div>

  <address class="contact">
    <div class="contact__address">18 Carden Ave.<br>Unit 7 Brampton, Ontario L6T 2K9</div>
    <ul class="contact__list">
      <li class="contact__item">
        <svg class="contact__icon" viewBox="0 0 16 16"><path d="M2 7c0-3 3-4 6-4s6 1 6 4l-3 1-1-2H6L5 8Z"/><rect x="4" y="9" width="8" height="5" rx="1"/></svg>
        555.204.3318 x 214
      </li>
      <li class="contact__item">
        <svg class="contact__icon" viewBox="0 0 16 16"><rect x="4" y="1" width="8" height="5"/><rect x="1" y="6" width="14" height="6" rx="1"/><rect x="4" y="11" width="8" height="4"/></svg>
        555.204.3390
      </li>
      <li class="contact__item">
        <svg class="contact__icon" viewBox="0 0 16 16"><rect x="4" y="1" width="8" height="14" rx="1.5"/><rect x="5.5" y="3" width="5" height="5" fill="#fff"/></svg>
        555.318.6642
      </li>
      <li class="contact__item">
        <svg class="contact__icon" viewBox="0 0 16 16"><rect x="1" y="1" width="14" height="14" rx="2"/><rect x="3" y="4" width="10" height="2" fill="#fff"/><rect x="3" y="9" width="10" height="2" fill="#fff"/></svg>
        1 800 555.0147
      </li>
      <li class="contact__item">
        <svg class="contact__icon" viewBox="0 0 16 16"><path d="M1 3h14v10H1Z" fill="none" stroke="var(--blue)" stroke-width="1.6"/><path d="M1 3l7 6 7-6" fill="none" stroke="var(--blue)" stroke-width="1.6"/></svg>
        dhollis@pineledgersystems.com
      </li>
    </ul>
  </address>

  <div class="person">
    <div class="person__name">Dana Hollis</div>
    <div class="person__role">Sales Manager</div>
  </div>
</section>

<section class="card card--back">
  <div class="footer-rule" aria-hidden="true"></div>
  <div class="footer-band" aria-hidden="true"></div>

  <div class="brand"><span class="brand__mark"></span>Pine Ledger Systems</div>

  <div class="website">www.pineledgersystems.com</div>
</section>

</body>
</html>
```